Modern, corporate management consultancy firm needs a new website

We need a website for an Australian based management consultancy firm.

The company name is Corbel Strategy Partners.

We are looking for a parallax style wordpress site.

The site needs to provide the following functions:

1) subscribe function
2) links to social media (twitter, linkedin and mail)
3) a gated document section where people can download pdf's from the site after registering or providing name, company, position, email and contact number.

Attached is the company logo, would like to see designs that incorporate the dark blue and silver in the logo and separated into the following sections (Home, About, Services (with 4 options), Our Team, Links, Contacts.

Need the site to be easy to navigate and updated.

Potentially a News Section that can be updated regularly.

Target Market(s)

Target market is SME, business owners and directors

Industry/Entity Type

Management Consulting

Coding

Coded - Design and coding required

Number of Pages Required

1 page

Font styles to use
Sans Serif

Colors
0255a3
cbcbcb
757575
000000

Requirements
Must have
• Must be easy to read and use
Nice to have
• Features are listed on initial brief

```html
<!DOCTYPE html>
<html lang="en">
<head>
<meta charset="utf-8">
<title>Corbel Strategy Partners</title>
<link href="https://fonts.googleapis.com/css2?family=Open+Sans:wght@400;600;700&display=swap" rel="stylesheet">
<style>
  :root {
    --blue: #0255a3;
    --navy: #0f2f52;
    --navy-deep: #0a223d;
    --silver: #cbcbcb;
    --grey: #757575;
    --black: #000000;
    --white: #ffffff;
    --pdf-red: #d9322b;
    --bar: #1f2327;
  }
  * { box-sizing: border-box; margin: 0; padding: 0; }
  html, body { width: 865px; height: 1200px; overflow: hidden; }
  body { font-family: "Open Sans", Arial, sans-serif; color: var(--grey); background: var(--white); position: relative; }

  /* Header */
  .site-header { position: absolute; top: 0; left: 0; width: 865px; height: 72px; display: flex; align-items: center; padding: 0 40px; background: var(--white); }
  .brand { display: flex; align-items: center; gap: 10px; }
  .brand-mark { width: 34px; height: 34px; border-radius: 50%; background: var(--navy); }
  .brand-name { font-size: 15px; font-weight: 600; color: var(--navy); line-height: 1.1; width: 120px; }
  .main-nav { display: flex; gap: 34px; margin-left: 160px; font-size: 10px; font-weight: 600; text-transform: uppercase; color: var(--grey); }
  .main-nav .active { color: var(--black); border-bottom: 2px solid var(--blue); padding-bottom: 3px; }
  .social { display: flex; gap: 7px; margin-left: auto; }
  .social span { width: 20px; height: 20px; border-radius: 50%; background: var(--blue); display: block; }

  /* Hero */
  .hero { position: absolute; top: 72px; left: 0; width: 865px; height: 331px; background: linear-gradient(120deg, #e9edf1 0%, #d4dade 35%, #c9b7a5 55%, #eef1f4 80%, #dfe4e8 100%); }
  .hero-title { position: absolute; top: 108px; left: 275px; width: 315px; height: 32px; background: var(--navy); color: var(--white); font-size: 19px; font-weight: 600; text-align: center; line-height: 32px; }
  .hero-text { position: absolute; top: 148px; left: 115px; width: 635px; padding: 10px 18px; background: rgba(2,85,163,0.78); color: var(--white); font-size: 11px; line-height: 1.5; text-align: center; }

  /* About */
  .about { position: absolute; top: 403px; left: 0; width: 865px; height: 245px; text-align: center; padding-top: 28px; }
  .section-title { font-size: 30px; font-weight: 400; color: var(--grey); }
  .about p { width: 620px; margin: 14px auto 0; font-size: 9.5px; line-height: 1.6; }
  .btn { display: inline-block; background: var(--navy); color: var(--white); font-size: 9px; font-weight: 600; text-transform: uppercase; padding: 7px 16px; }
  .about .btn { margin-top: 22px; }

  /* Newsletter */
  .newsletter { position: absolute; top: 648px; left: 0; width: 865px; height: 268px; background: radial-gradient(ellipse at 50% 40%, #1d4c7c 0%, var(--navy) 55%, var(--navy-deep) 100%); text-align: center; }
  .newsletter h2 { margin-top: 40px; font-size: 24px; font-weight: 400; color: var(--white); letter-spacing: 1px; text-transform: uppercase; }
  .fields { position: absolute; top: 115px; left: 130px; display: flex; gap: 14px; }
  .field { width: 296px; height: 32px; background: var(--navy-deep); border: 1px solid #5a7391; color: var(--silver); font-size: 10px; text-align: left; padding: 0 10px; line-height: 30px; }
  .signup { position: absolute; top: 184px; left: 337px; width: 190px; height: 38px; background: var(--blue); color: var(--white); font-size: 20px; font-weight: 600; line-height: 38px; text-transform: uppercase; }

  /* Downloads */
  .downloads { position: absolute; top: 916px; left: 0; width: 865px; height: 135px; }
  .doc { position: absolute; top: 40px; display: flex; gap: 18px; }
  .doc-one { left: 80px; }
  .doc-two { left: 470px; }
  .doc-text { font-size: 9.5px; font-weight: 600; color: var(--blue); width: 250px; padding-top: 6px; }
  .doc-text .btn { margin-top: 14px; padding: 6px 16px; }

  /* Footer */
  .site-footer { position: absolute; top: 1051px; left: 0; width: 865px; height: 129px; background: var(--white); border-top: 1px solid #e3e3e3; }
  .footer-links { position: absolute; top: 36px; left: 84px; font-size: 10px; color: var(--grey); }
  .footer-links span { margin: 0 5px; }
  .site-footer .social { position: absolute; top: 62px; left: 84px; }
  .site-footer .brand { position: absolute; top: 38px; left: 575px; }
  .site-footer .brand-mark { width: 44px; height: 44px; }
  .site-footer .brand-name { font-size: 18px; width: 170px; }
  .copyright { position: absolute; top: 1180px; left: 0; width: 865px; height: 20px; background: var(--bar); color: var(--silver); font-size: 8px; line-height: 20px; padding-left: 84px; }
</style>
</head>
<body>

<header class="site-header">
  <div class="brand"><span class="brand-mark"></span><span class="brand-name">Corbel Strategy Partners</span></div>
  <nav class="main-nav">
    <span class="active">Home</span><span>About</span><span>Services</span><span>Our Team</span><span>Link</span>
  </nav>
  <div class="social"><span></span><span></span><span></span></div>
</header>

<section class="hero" role="img" aria-label="Photograph of business people's hands working over a tablet and papers on a desk">
  <h1 class="hero-title">Lorem Ipsum is simply dummy</h1>
  <p class="hero-text">Lorem Ipsum is simply dummy text of the printing and typesetting industry. Lorem Ipsum has been the industry's standard dummy text ever since. Lorem Ipsum is simply dummy text ever.</p>
</section>

<section class="about">
  <h2 class="section-title">About Us</h2>
  <p>Lorem Ipsum is simply dummy text of the printing and typesetting industry. Lorem Ipsum has been the industry's standard dummy text ever since the 1500s, when an unknown printer took a galley of type and scrambled it to make a type specimen book.</p>
  <p>It has survived not only five centuries, but also the leap into electronic typesetting, remaining essentially unchanged and widely used today.</p>
  <span class="btn">Read More</span>
</section>

<section class="newsletter" role="img" aria-label="Dark blue toned photograph of a business meeting behind the sign-up form">
  <h2>News Latter Sign Up</h2>
  <div class="fields"><div class="field">Email...</div><div class="field">Password...</div></div>
  <div class="signup">Signup</div>
</section>

<section class="downloads">
  <div class="doc doc-one">
    <svg width="44" height="54" viewBox="0 0 44 54" aria-hidden="true">
      <path d="M2 2h28l12 12v38H2z" fill="none" stroke="var(--pdf-red)" stroke-width="3"/>
      <path d="M30 2v12h12" fill="none" stroke="var(--pdf-red)" stroke-width="3"/>
      <rect x="0" y="26" width="38" height="16" fill="var(--pdf-red)"/>
      <text x="19" y="38" text-anchor="middle" font-family="Open Sans, sans-serif" font-size="11" font-weight="700" fill="#fff">PDF</text>
    </svg>
    <div class="doc-text">Lorem Ipsum is simply dummy emet ipsum is simply dummy<br><span class="btn">Download</span></div>
  </div>
  <div class="doc doc-two">
    <svg width="44" height="54" viewBox="0 0 44 54" aria-hidden="true">
      <path d="M2 2h28l12 12v38H2z" fill="none" stroke="var(--pdf-red)" stroke-width="3"/>
      <path d="M30 2v12h12" fill="none" stroke="var(--pdf-red)" stroke-width="3"/>
      <rect x="0" y="26" width="38" height="16" fill="var(--pdf-red)"/>
      <text x="19" y="38" text-anchor="middle" font-family="Open Sans, sans-serif" font-size="11" font-weight="700" fill="#fff">PDF</text>
    </svg>
    <div class="doc-text">Lorem Ipsum is simply dummyemet ipsum is simply dummy<br><span class="btn">Download</span></div>
  </div>
</section>

<footer class="site-footer">
  <div class="footer-links">Home<span>|</span>About Us<span>|</span>Services<span>|</span>Product<span>|</span>Contact Us</div>
  <div class="social"><span></span><span></span><span></span></div>
  <div class="brand"><span class="brand-mark"></span><span class="brand-name">Corbel Strategy Partners</span></div>
</footer>
<div class="copyright">Copyright © 2024 Corbel Strategy Partners. All rights reserved.</div>

</body>
</html>
```